Torvane Staffing - Mission Poster Design

We are a staffing and recruiting firm with multiple locations across the US. I am seeking a clean modern design highlighting our Mission Statement: Torvane Staffing...Linking Bright Talent with Bold Employers! This design will be framed and placed at the entrance of all of our offices. My website is www.torvanestaffing.example

Target Market(s)

Will be our company mission with a poster prominently placed in each office.

Industry/Entity Type

Staffing

Requirements
Must have
• Must be professional, clean and eye catching. We want to embrace diversity, so we like a variety of people if people will be a focal part.

```html
<!DOCTYPE html>
<html lang="en">
<head>
<meta charset="utf-8">
<title>Torvane Staffing – Mission Poster</title>
<link href="https://fonts.googleapis.com/css2?family=Arimo:wght@400;700&display=swap" rel="stylesheet">
<style>
  :root {
    --navy: #29256a;
    --yellow: #ecc41f;
    --green: #137d40;
    --red: #e8302c;
    --white: #ffffff;
    --ink: #222222;
    --stage: #e8e6e2;
  }
  html, body {
    margin: 0;
    padding: 0;
    width: 1200px;
    height: 2394px;
    overflow: hidden;
    background: var(--stage);
  }
  .poster {
    position: absolute;
    left: 40px;
    top: 450px;
    width: 1120px;
    height: 1493px;
    background: var(--white);
    box-shadow: 0 6px 24px rgba(0,0,0,0.18);
    overflow: hidden;
    font-family: "Arimo", Arial, sans-serif;
  }
  .poster__bands {
    position: absolute;
    inset: 0;
    width: 100%;
    height: 100%;
  }
  .brand-name {
    position: absolute;
    top: 110px;
    left: 0;
    width: 100%;
    text-align: center;
    font-size: 100px;
    font-weight: 400;
    color: var(--white);
    letter-spacing: -1px;
    margin: 0;
    line-height: 1;
  }
  .mission {
    position: absolute;
    top: 318px;
    left: 0;
    width: 100%;
    text-align: center;
    color: var(--white);
    margin: 0;
    font-weight: 400;
  }
  .mission__line { display: block; }
  .mission__line--first { font-size: 66px; line-height: 76px; }
  .mission__line--second { font-size: 58px; line-height: 72px; }
  .mission__accent { font-weight: 700; }
  .mission__accent--yellow { color: var(--yellow); }
  .mission__accent--red { color: var(--red); }
  .crowd-photo {
    position: absolute;
    left: 105px;
    top: 816px;
    width: 935px;
    height: 565px;
    border-radius: 60px 60px 30px 30px;
    background:
      radial-gradient(ellipse at 50% 40%, rgba(214,170,140,0.85), rgba(214,170,140,0) 60%),
      linear-gradient(90deg, #c9623a 0%, #3b4f86 22%, #b9383a 45%, #6f8fbf 62%, #b52b36 75%, #3c5aa8 100%);
    opacity: 0.85;
  }
  .website {
    position: absolute;
    top: 1388px;
    left: 0;
    width: 100%;
    text-align: center;
    font-size: 45px;
    color: var(--ink);
    margin: 0;
  }
  .website__domain { font-weight: 700; color: var(--green); }
</style>
</head>
<body>
  <main class="poster">
    <svg class="poster__bands" viewBox="0 0 803 1070" preserveAspectRatio="none" aria-hidden="true">
      <polygon fill="var(--navy)" points="0,0 803,0 803,307 416,527 0,287"/>
      <polygon fill="var(--yellow)" points="0,287 416,527 362,557 0,357"/>
      <polygon fill="var(--green)" points="803,307 416,527 476,557 803,377"/>
    </svg>

    <p class="brand-name">Torvane Staffing</p>

    <h1 class="mission">
      <span class="mission__line mission__line--first">Linking <span class="mission__accent mission__accent--yellow">Bright Talent</span></span>
      <span class="mission__line mission__line--second">with <span class="mission__accent mission__accent--red">Bold Employers!</span></span>
    </h1>

    <div class="crowd-photo" role="img" aria-label="Photo of a large, diverse crowd of people standing together and looking up"></div>

    <p class="website">www.<span class="website__domain">torvanestaffing</span>.example</p>
  </main>
</body>
</html>
```